Vemtra Group: Business Card for a high end technology company

We need a cool new design for our business cards using our cloud logo. We are a technology consulting business. We pride ourselves on be the best of the best. We mainly focus on cloud solutions and managed services. We need a business card that sets us apart from the other technology companies in the area and allows us to stand out.

Target Market(s)

Technology departments, CIO, CEOs, and Information Technology Staff.

Industry/Entity Type

Information Technology

Contact Information for Business Card

Must have the logo and our name.
Must have employee name, email address, office phone, cell phone and website.
Need to have all info on one side a cool design on backside.

Font styles to use
Serif
Sans Serif

Requirements
Must have
• Must have the logo and our name.
• Must have employee name, email address, office phone, cell phone and website.
• Need to have all info on one side a cool design on back side.
• Must be a crisp clean design, not too busy or confusing.

```html
<!DOCTYPE html>
<html lang="en">
<head>
<meta charset="UTF-8">
<title>Vemtra Group – Business Card</title>
<link rel="stylesheet" href="https://fonts.googleapis.com/css2?family=Open+Sans:wght@400;600;700&display=swap">
<style>
  :root {
    --card-bg: #bbeef5;
    --ink: #000000;
    --brand-grey: #444444;
    --brand-url: #333333;
    --brand-blue: #2f9ce8;
  }
  html, body {
    margin: 0;
    padding: 0;
    overflow: hidden;
  }
  .card {
    position: relative;
    width: 1200px;
    height: 720px;
    background: var(--card-bg);
    font-family: "Open Sans", sans-serif;
    color: var(--ink);
    overflow: hidden;
  }
  .employee-name {
    position: absolute;
    left: 12px;
    top: 48px;
    margin: 0;
    font-size: 100px;
    font-weight: 400;
    line-height: 1.2;
    letter-spacing: -1px;
    white-space: nowrap;
  }
  .rule {
    position: absolute;
    left: 20px;
    width: 788px;
    height: 5px;
    background: var(--ink);
  }
  .contact-line {
    position: absolute;
    left: 20px;
    margin: 0;
    font-size: 53px;
    font-weight: 400;
    line-height: 1;
    white-space: nowrap;
  }
  .brand-mark {
    position: absolute;
    left: 950px;
    top: 420px;
    width: 120px;
    height: 120px;
    border-radius: 50%;
    background: var(--brand-blue);
  }
  .brand-name {
    position: absolute;
    left: 830px;
    top: 585px;
    width: 360px;
    margin: 0;
    font-size: 48px;
    font-weight: 400;
    line-height: 1;
    color: var(--brand-grey);
    text-align: center;
    white-space: nowrap;
  }
  .brand-url {
    position: absolute;
    left: 830px;
    top: 645px;
    width: 360px;
    margin: 0;
    font-size: 17px;
    font-weight: 700;
    line-height: 1;
    color: var(--brand-url);
    text-align: center;
    letter-spacing: 0.5px;
    white-space: nowrap;
  }
</style>
</head>
<body>
  <main class="card">
    <h1 class="employee-name">EMPLOYEE NAME</h1>

    <div class="rule" style="top:172px"></div>
    <p class="contact-line" style="top:189px">Email - employee@domain.com</p>
    <div class="rule" style="top:261px"></div>

    <div class="rule" style="top:300px"></div>
    <p class="contact-line" style="top:317px">Office Phone - 777-777-7777</p>
    <div class="rule" style="top:390px"></div>

    <div class="rule" style="top:426px"></div>
    <p class="contact-line" style="top:445px">Cell Phone - 555-555-5555</p>
    <div class="rule" style="top:516px"></div>

    <div class="rule" style="top:552px"></div>
    <p class="contact-line" style="top:573px">Website - www.website.com</p>
    <div class="rule" style="top:641px"></div>

    <div class="brand-mark" aria-hidden="true"></div>
    <p class="brand-name">Vemtra Group</p>
    <p class="brand-url">www.vemtragroup.com</p>
  </main>
</body>
</html>
```